KL Taxidermy

I need business Cards with my logo and a background photo of one of my taxidermy mounts.
I would like a black back drop behind it all and what ever looks best for my contact information (red or white?)
Garrick Pembley
592-718-4409
kltaxidermy482@mailnook.example
Chatterloom page

```html
<!DOCTYPE html>
<html lang="en">
<head>
<meta charset="utf-8">
<title>KL Taxidermy – Business Cards</title>
<link rel="stylesheet" href="https://fonts.googleapis.com/css2?family=Oswald:wght@700&family=Open+Sans:wght@400;700&display=swap">
<style>
  :root {
    --bg: #d9d6d1;
    --card-black: #0b0b0b;
    --card-sheen: #1c1c1c;
    --ink-white: #ffffff;
    --ink-soft: #e6e6e6;
    --photo-light: #8d8a86;
    --photo-dark: #2a2a2a;
  }
  * { margin: 0; padding: 0; box-sizing: border-box; }
  html, body { width: 1200px; height: 942px; overflow: hidden; background: var(--bg); }
  .sheet { position: relative; width: 1200px; height: 942px; }
  .card {
    position: absolute; left: 250px; width: 700px; height: 400px;
    background: linear-gradient(135deg, var(--card-sheen) 0%, var(--card-black) 55%);
    overflow: hidden; box-shadow: 0 10px 30px rgba(0,0,0,.35);
  }
  .card--front { top: 50px; }
  .card--back { top: 492px; }

  .brand {
    display: flex; align-items: center; gap: 12px; white-space: nowrap;
    font-family: "Open Sans", sans-serif; font-weight: 700;
    color: var(--ink-white); text-transform: uppercase; letter-spacing: 2px;
  }
  .brand__dot { width: 16px; height: 16px; border-radius: 50%; background: var(--ink-white); flex: none; }

  .card--front .brand { position: absolute; left: 50px; top: 185px; font-size: 22px; }
  .divider { position: absolute; left: 310px; top: 70px; width: 2px; height: 260px; background: var(--ink-soft); }

  .contact { position: absolute; left: 340px; top: 112px; width: 335px; color: var(--ink-white); }
  .contact__name {
    font-family: "Oswald", sans-serif; font-weight: 700; font-size: 32px;
    letter-spacing: 2px; text-transform: uppercase; margin-bottom: 18px; white-space: nowrap;
  }
  .contact__row {
    display: flex; align-items: center; gap: 10px; white-space: nowrap;
    font-family: "Open Sans", sans-serif; font-size: 17px; margin-bottom: 10px;
  }
  .contact__icon { width: 18px; height: 18px; flex: none; }
  .contact__square { width: 16px; height: 16px; margin: 0 1px; background: var(--ink-white); flex: none; }

  .mount-photo {
    position: absolute; inset: 0;
    background: radial-gradient(ellipse 45% 75% at 48% 50%, var(--photo-light) 0%, var(--photo-dark) 60%, var(--card-black) 100%);
  }
  .card--back .brand { position: absolute; left: 50%; top: 50%; transform: translate(-50%, -50%); font-size: 34px; }
</style>
</head>
<body>
<main class="sheet">
  <section class="card card--front">
    <div class="brand"><span class="brand__dot"></span>KL Taxidermy</div>
    <div class="divider"></div>
    <div class="contact">
      <div class="contact__name">Garrick Pembley</div>
      <div class="contact__row">
        <svg class="contact__icon" viewBox="0 0 20 20"><rect width="20" height="20" rx="3" fill="#fff"/><path d="M6 4c1 0 2 2.5 2 3s-1 1-1 1.5c.5 1.5 2 3 3.5 3.5.5 0 1-1 1.5-1s3 1 3 2-1.5 2.5-2.5 2.5C8 15.5 4.5 12 4.5 6.5 4.5 5.5 5 4 6 4z" fill="#0b0b0b"/></svg>
        592-718-4409
      </div>
      <div class="contact__row">
        <svg class="contact__icon" viewBox="0 0 20 20"><rect x="1" y="4" width="18" height="12" fill="#fff"/><path d="M1 4l9 7 9-7" fill="none" stroke="#0b0b0b" stroke-width="1.5"/></svg>
        kltaxidermy482@mailnook.example
      </div>
      <div class="contact__row">
        <span class="contact__square"></span>
        Chatterloom page
      </div>
    </div>
  </section>

  <section class="card card--back">
    <div class="mount-photo" role="img" aria-label="Photo of a white ram taxidermy mount on a dark backdrop"></div>
    <div class="brand"><span class="brand__dot"></span>KL Taxidermy</div>
  </section>
</main>
</body>
</html>
```